Lantern Lane Town Footpath Chronicle Trek

We are launching a different kind of city historical walking tour company with a slightly darker approach using historical but real stories that have long been forgotten from living memory.
Our tour is going to contain a lot of very thoroughly researched stories ranging from 50 to 150 years past that takes the customer into the actual-real life past of the city streets.  Stories that may contains some dark undertones and stories with a twist or that seem eccentric to us now but were entirely normal back in olden times - minus the dry historical facts that most tours engage in..
Our tours are going to run both day and night and will incorporate real history / real Lantern Lane, so some of the stories will be quite serious (e.g.- there are actual murders from 100 years ago, baffling court cases, even a bit of poetry written by murderers, suicides, love triangles, you name it.  We are aiming for a mystery/history theme and are aiming to attract tourists who are interested in getting a different kind of history.

We're not going for scares and even though we expect people to enjoy our tours;  we're not aiming at light fun and frivolity.  I guess if you wanted to give us a tv rating we'd be aiming at M to MA15+.
If I was to give you another analogy using the literature world.  Think Edwin Harrowgates Nocturno rather than the Moonrise Saga of movies.  Or Clara Wendham's Gravemoor rather than the Pickwells.  Even Crown of Embers rather than a soap opera.
Our stories are being carefully crafted and are packed with unexpected twists, turns & revelations whilst remaining all 100% true.  We have approx 15-20 stories for each tour and we're designing them in a way that each story will trigger a different range of emotions in the listeners on a regular basis.  We're being very careful to keep it fresh for each story so that it will next to impossible for our guests to zone out!  I personally can't stand going on a tour where mildly interesting facts are read out.  We like deep, rich stories rather than pop entertainment.
We want the website to generate a feeling/atmosphere for our product that draws the right crowd to our tours as well as making it easy to make a booking.  Basic features to include:-
Home Page
Bookings Page
Integration with a booking system will be required here via use of plugin code.
Private Functions Page
We are hoping to integrate with a booking system via use of plugin code.  If not, then a simple form enquiry type input e.g.- name, emails, subject, contact, details, preferred date/time, etc).
About Us Page :-
Dark; a euphemism for the unknown or the forgotten.  Think dark ages, dark matter, dark energy; things where knowledge is uncertain or unknown are often termed dark.   Lantern lane brings back the hidden past, the forgotten past, the past that may not want to be remembered……but these are real stories....real stories that come from the streets around you.

Some of these stories may be tales of dark things.....some may simply be a charming reminder of days gone by…..regardless these stories are compelling reminders of the amazing times that precede us…..and the forgotten people of yesteryear finally get a chance to have their story told to a fresh audience.  Through you, the people of yesterday get to live again.  Will you like what you hear?

Contact Us page:-
•	A form input type page.
•	Include space for our phone number
•	Include space for our email address
Other Items:-
Social Media Links; we will be looking for social media icons to link to our social media pages to Chatterbook, Snapfolio, Chirplet.
Subscription; we want to also capture an input email address box for site visitors.  We will be launching a weekly Lantern Lane podcast / email newsetter; with a weekly Lantern Lane from a different place in the world and we want some way for people to subscribe.

Updates
Project Deadline Extended
Reason: A few additional photos have been uploaded.  Feel free to utilize if helpful.  Our stories range from the 1800s to 1950s in an era with beautiful old Victorian buildings.  I'm putting through the extension just to give some more time to see if this gives any more ideas and inspiration.  Thank you for all the great submissions.

Target Market(s)
Tourists that want to hear a darker version of the city they are visiting. Stories that other tour companies would not even think of covering. The real history of the events that ordinary people lived through that didn't necessarily make the history books. All stories are true; as per project description.
Industry/Entity Type
Tourism
Coding
Coded - Design and coding required
Number of Pages Required
5+ page
Colors
Designer to choose colors to be used in the design.
Look and feel

```html
<!DOCTYPE html>
<html lang="en">
<head>
<meta charset="utf-8">
<title>Lantern Lane Town Footpath Chronicle Trek</title>
<link rel="stylesheet" href="https://fonts.googleapis.com/css2?family=Gochi+Hand&family=Roboto+Slab:wght@400;700&display=swap">
<style>
:root{
  --red:#e0252c;
  --black:#0b0b0b;
  --ink:#222;
  --paper:#e4e5e6;
  --paper-dark:#d9dadb;
  --slate:#5d6a70;
  --newsletter:#8d8f90;
  --white:#fff;
  --muted:#777;
  --hand:"Gochi Hand",cursive;
  --slab:"Roboto Slab",serif;
}
*{box-sizing:border-box;margin:0;padding:0}
html,body{width:1200px;height:3913px;overflow:hidden}
body{font-family:var(--slab);color:var(--ink);background:var(--paper);position:relative}
.abs{position:absolute}
.photo{position:absolute;overflow:hidden}

/* hero */
.hero{position:absolute;left:0;top:0;width:1200px;height:483px;
  background:linear-gradient(180deg,#c8553a 0%,#e0703f 30%,#8a2a22 62%,#3a120f 100%)}
.hero-temple{position:absolute;right:0;top:40px;width:640px;height:443px;
  background:linear-gradient(200deg,#4a1a10 0%,#a8381e 45%,#d7642a 70%,#3b110c 100%);opacity:.75}
.logo{position:absolute;left:84px;top:14px;display:flex;align-items:center;gap:10px}
.logo-dot{width:40px;height:40px;border-radius:50%;background:var(--white)}
.logo-name{font-family:var(--slab);font-weight:700;font-size:18px;color:var(--white)}
.nav{position:absolute;left:540px;top:0;width:620px;height:73px;background:rgba(20,20,20,.82);
  border-radius:0 0 0 14px;display:flex;align-items:center;gap:28px;padding-left:48px}
.nav a{color:var(--white);text-decoration:none;font-size:14px}
.nav a.active{border-bottom:2px solid var(--white);padding-bottom:4px}
.hero-title{position:absolute;left:0;width:1200px;top:165px;text-align:center;color:var(--white)}
.hero-title h1{font-family:var(--hand);font-weight:400;font-size:62px;line-height:1;letter-spacing:1px}
.hero-title p{font-family:var(--slab);font-size:30px;margin-top:6px}
.btn-red{background:var(--red);color:var(--white);font-family:var(--slab);font-size:15px;border:none;
  display:flex;align-items:center;justify-content:center}
.book-now{position:absolute;left:527px;top:318px;width:141px;height:40px;border-radius:4px}

/* search */
.search{position:absolute;left:0;top:483px;width:1200px;height:227px;background:var(--black)}
.field{position:absolute;height:58px;background:var(--white);border-radius:2px;font-size:13px;color:#555;
  display:flex;align-items:center;padding-left:16px}
.field svg{position:absolute;right:14px;top:25px}
.range{position:absolute;left:611px;top:138px;width:234px}
.range-track{height:4px;background:var(--red);margin:0 8px;position:relative;top:0}
.range-knob{position:absolute;top:-7px;width:18px;height:18px;border-radius:50%;background:var(--red)}
.range-labels{display:flex;justify-content:space-between;color:var(--white);font-size:12px;margin-top:18px}
.search-btn{position:absolute;left:869px;top:605px;width:237px;height:58px;font-size:16px}

/* features */
.features{position:absolute;left:0;top:710px;width:1200px;height:1132px;background:var(--paper)}
.tile{position:absolute;color:var(--white);display:flex;flex-direction:column;align-items:center;justify-content:center;text-align:center}
.tile h3{font-family:var(--hand);font-weight:400;line-height:1}
.tile p{font-size:13px;margin-top:6px}
.section-title{position:absolute;left:0;width:1200px;text-align:center;font-family:var(--hand);font-weight:400;font-size:50px;color:var(--ink)}
.title-rule{position:absolute;left:570px;width:60px;height:2px;background:var(--red)}
.subtitle{position:absolute;left:0;width:1200px;text-align:center;font-size:16px;color:var(--muted)}
.dest-card{position:absolute;top:1453px;width:316px;height:298px;border:5px solid var(--white);box-shadow:0 2px 6px rgba(0,0,0,.2);
  display:flex;flex-direction:column;align-items:center;justify-content:flex-end;padding-bottom:40px;color:var(--white)}
.dest-card h4{font-family:var(--hand);font-weight:400;font-size:36px;line-height:1}
.dest-card p{font-size:12px}
.arrow-btn{position:absolute;width:44px;height:44px;border-radius:50%;background:var(--white);
  box-shadow:0 1px 4px rgba(0,0,0,.3);display:flex;align-items:center;justify-content:center}

/* gallery */
.gallery{position:absolute;left:0;top:1842px;width:1200px;height:981px;
  background:linear-gradient(180deg,#4f5d64 0%,#687880 60%,#566369 100%)}
.gallery .section-title{color:var(--white);top:90px}
.gallery-desc{position:absolute;left:340px;width:520px;top:195px;text-align:center;color:var(--white);font-size:12px;line-height:1.6}
.filters{position:absolute;left:0;width:1200px;top:278px;display:flex;justify-content:center;gap:12px}
.filters span{background:var(--white);color:#444;font-size:11px;padding:6px 16px;border-radius:14px;text-transform:uppercase}
.filters span.on{background:var(--red);color:var(--white)}
.caption{position:absolute;left:0;top:2343px;width:297px;height:78px;background:var(--white);text-align:center}
.caption b{display:block;font-size:12px;margin-top:24px;font-weight:700}
.caption small{font-size:10px;color:var(--muted)}
.caption i{position:absolute;left:138px;top:-11px;width:22px;height:22px;border-radius:50%;background:var(--red)}
.load-more{position:absolute;left:543px;top:2702px;width:130px;height:38px;border-radius:3px;font-size:14px}

/* podcast */
.podcast{position:absolute;left:0;top:2823px;width:1200px;height:381px;background:var(--paper-dark)}
.pod-item{position:absolute;top:3040px;width:320px;height:73px;display:flex;gap:26px}
.pod-thumb{width:78px;height:70px;position:relative;flex:none}
.pod-thumb i{position:absolute;left:28px;top:24px;width:22px;height:22px;border-radius:50%;background:var(--red)}
.pod-item h5{font-size:12px;font-weight:400;text-transform:uppercase;line-height:1.5;color:#333;margin-top:4px}
.pod-item small{font-size:10px;color:var(--muted);display:block;margin-top:10px}

/* newsletter */
.newsletter{position:absolute;left:0;top:3204px;width:1200px;height:428px;background:var(--newsletter)}
.newsletter .section-title{color:var(--white);top:80px}
.news-text{position:absolute;left:0;width:1200px;top:196px;text-align:center;color:var(--white);font-size:17px}
.news-small{position:absolute;left:0;width:1200px;top:228px;text-align:center;color:var(--white);font-size:11px}
.email-box{position:absolute;left:347px;top:3496px;width:323px;height:47px;background:var(--white);font-size:13px;color:#777;
  display:flex;align-items:center;padding-left:18px}
.subscribe{position:absolute;left:670px;top:3496px;width:186px;height:47px;font-size:14px;text-transform:uppercase}

/* footer */
.footer{position:absolute;left:0;top:3632px;width:1200px;height:281px;background:var(--black);color:var(--white)}
.foot-col{position:absolute;top:46px}
.foot-col h6{font-size:19px;font-weight:400;margin-bottom:10px}
.foot-col li{list-style:none;font-size:11px;line-height:18px;color:#ddd}
.contact li{display:flex;align-items:center;gap:8px}
.social{display:flex;gap:8px;margin-top:6px;font-size:10px;color:#ddd}
.foot-bar{position:absolute;left:0;top:234px;width:1200px;border-top:1px solid #333}
.copyright{position:absolute;left:99px;top:250px;font-size:10px;color:#ccc}
.pay{position:absolute;right:80px;top:246px;display:flex;gap:16px;font-size:12px;color:#bbb}
</style>
</head>
<body>

<header class="hero">
  <div class="hero-temple" role="img" aria-label="Old wooden temple on a hillside glowing at sunset over a city"></div>
  <div class="logo"><span class="logo-dot"></span><span class="logo-name">Lantern Lane</span></div>
  <nav class="nav">
    <a class="active" href="#">Home</a><a href="#">Bookings</a><a href="#">Private Functions</a><a href="#">About us</a><a href="#">Contact us</a>
    <svg width="16" height="16" viewBox="0 0 16 16"><circle cx="6.5" cy="6.5" r="5" fill="none" stroke="#fff" stroke-width="2"/><path d="M10 10l5 5" stroke="#fff" stroke-width="2"/></svg>
  </nav>
  <div class="hero-title">
    <h1>Adventures Tour with</h1>
    <p>Real Life Stories</p>
  </div>
  <a class="btn-red book-now">Book Now</a>
  <svg class="abs" style="left:585px;top:448px" width="30" height="20" viewBox="0 0 30 20"><path d="M3 4l12 12 12-12" fill="none" stroke="#fff" stroke-width="4"/></svg>
</header>

<section class="search">
  <div class="field" style="left:99px;top:65px;width:235px">Activity<svg width="8" height="5"><path d="M0 0h8L4 5z" fill="#999"/></svg></div>
  <div class="field" style="left:355px;top:65px;width:235px">Destination<svg width="8" height="5"><path d="M0 0h8L4 5z" fill="#999"/></svg></div>
  <div class="field" style="left:611px;top:65px;width:234px">Your Location<svg width="8" height="5"><path d="M0 0h8L4 5z" fill="#999"/></svg></div>
  <div class="field" style="left:869px;top:65px;width:237px">Duration<svg width="8" height="5"><path d="M0 0h8L4 5z" fill="#999"/></svg></div>
  <div class="field" style="left:99px;top:122px;width:235px">No of People<svg width="8" height="5"><path d="M0 0h8L4 5z" fill="#999"/></svg></div>
  <div class="field" style="left:355px;top:122px;width:235px">Departure<svg width="8" height="5"><path d="M0 0h8L4 5z" fill="#999"/></svg></div>
  <div class="range">
    <div class="range-track"><span class="range-knob" style="left:-9px"></span><span class="range-knob" style="right:-9px"></span></div>
    <div class="range-labels"><span>0 USD</span><span>150,000 USD</span></div>
  </div>
</section>
<a class="btn-red search-btn">SEARCH</a>

<section class="features"></section>
<div class="tile photo" style="left:99px;top:796px;width:582px;height:425px;background:radial-gradient(circle at 50% 30%,#8fb3c2 0%,#2a4a5a 35%,#0d1418 80%)" role="img" aria-label="Looking up through a dark rock cave towards daylight">
  <h3 style="font-size:62px">Rock Tour</h3><p style="font-size:16px">Enjoy The Trip</p>
</div>
<div class="tile photo" style="left:691px;top:796px;width:410px;height:206px;background:linear-gradient(160deg,#1d3a28 0%,#3f7a5a 50%,#13303a 100%)" role="img" aria-label="Turquoise underground cave pool">
  <h3 style="font-size:34px">Deep underground</h3><p style="font-size:11px">Experience The Adventure</p>
</div>
<div class="tile photo" style="left:691px;top:1015px;width:410px;height:206px;background:linear-gradient(180deg,#9cc3e0 0%,#d8c3a0 50%,#6f7f86 100%)" role="img" aria-label="Stone bridge over a canal with a gondola">
  <h3 style="font-size:34px">Canal Grande</h3><p style="font-size:11px">Experience The Venice</p>
</div>

<h2 class="section-title" style="top:1310px">Destination</h2>
<div class="title-rule" style="top:1385px"></div>
<p class="subtitle" style="top:1407px">Trending destinations Of 2017 in the World!</p>
<div class="dest-card photo" style="left:99px;background:linear-gradient(180deg,#d8b9d2 0%,#c9a38b 45%,#6f8e3c 100%)" role="img" aria-label="Domed tomb among gardens with birds in the sky"></div>
<div class="dest-card photo" style="left:438px;background:radial-gradient(circle at 50% 40%,#e8f3a0 0%,#7fae3a 40%,#2b5418 100%)" role="img" aria-label="Green forest tunnel glowing with light">
  <h4>America</h4><p>A Breath Of Fresh Air</p>
</div>
<div class="dest-card photo" style="left:785px;background:linear-gradient(180deg,#f0c79a 0%,#b89579 50%,#6a5647 100%)" role="img" aria-label="Hillside old city of stone buildings">
  <h4>Canada</h4><p>Old City Streets</p>
</div>
<div class="arrow-btn" style="left:77px;top:1580px"><svg width="10" height="14"><path d="M8 1L2 7l6 6" fill="none" stroke="#333" stroke-width="2"/></svg></div>
<div class="arrow-btn" style="left:1079px;top:1580px"><svg width="10" height="14"><path d="M2 1l6 6-6 6" fill="none" stroke="#333" stroke-width="2"/></svg></div>

<section class="gallery">
  <h2 class="section-title">Our Gallery</h2>
  <div class="title-rule" style="top:160px"></div>
  <p class="gallery-desc">A lot of very thoroughly researched stories ranging from 50 to 150 years past that takes the customer into the actual real life past of the city streets</p>
  <div class="filters"><span class="on">Show All</span><span>Hiking</span><span>Edition</span><span>General</span><span>Wildlife</span><span>Videos</span><span>Styling</span></div>
</section>
<div class="photo" style="left:0;top:2181px;width:297px;height:162px;background:linear-gradient(180deg,#4a5f8a 0%,#d69a5a 60%,#3a3040 100%)" role="img" aria-label="Domed city skyline beside a river at dusk"></div>
<div class="caption"><i></i><b>Rome</b><small>Sunset | Rome Tour</small></div>
<div class="photo" style="left:0;top:2426px;width:297px;height:240px;background:linear-gradient(180deg,#c8d3de 0%,#8a7a6e 55%,#7a3a2a 100%)" role="img" aria-label="Mountain village with snowy peaks"></div>
<div class="photo" style="left:300px;top:2181px;width:297px;height:485px;background:linear-gradient(180deg,#e8e2c2 0%,#7f8f5a 40%,#3b5a3a 75%,#5a6a6a 100%)" role="img" aria-label="Misty forest above a river valley"></div>
<div class="photo" style="left:600px;top:2181px;width:297px;height:485px;background:linear-gradient(180deg,#4f86d4 0%,#a6c3e6 30%,#5b5a48 55%,#3f6a2a 100%)" role="img" aria-label="Ancient stone pyramid temple in a jungle clearing"></div>
<div class="photo" style="left:900px;top:2181px;width:300px;height:240px;background:linear-gradient(180deg,#2a2a28 0%,#5a5438 60%,#1c1c1a 100%)" role="img" aria-label="Old off-road jeep at night"></div>
<div class="photo" style="left:900px;top:2426px;width:300px;height:240px;background:linear-gradient(180deg,#e8e690 0%,#8fa848 50%,#3a5a22 100%)" role="img" aria-label="Sunlit forest of tall trees"></div>
<a class="btn-red load-more">LOAD MORE</a>

<section class="podcast">
  <h2 class="section-title" style="top:80px">Lantern Lane podcast</h2>
  <div class="title-rule" style="top:165px"></div>
</section>
<svg class="abs" style="left:72px;top:3066px" width="10" height="16"><path d="M9 1L2 8l7 7" fill="none" stroke="#222" stroke-width="3"/></svg>
<svg class="abs" style="left:1116px;top:3066px" width="10" height="16"><path d="M1 1l7 7-7 7" fill="none" stroke="#222" stroke-width="3"/></svg>
<div class="pod-item" style="left:99px"><div class="pod-thumb photo" style="background:linear-gradient(160deg,#1a2430,#4a5a66)" role="img" aria-label="Podcast episode cover"><i></i></div><div><h5>Lorem ipsum is simply dummy text</h5><small>2800 Plays</small></div></div>
<div class="pod-item" style="left:451px"><div class="pod-thumb photo" style="background:linear-gradient(160deg,#14202e,#3a5068)" role="img" aria-label="Podcast episode cover"><i></i></div><div><h5>Lorem ipsum is simply dummy text</h5><small>2800 Plays</small></div></div>
<div class="pod-item" style="left:801px"><div class="pod-thumb photo" style="background:linear-gradient(160deg,#222,#555)" role="img" aria-label="Podcast episode cover"><i></i></div><div><h5>Lorem ipsum is simply dummy text</h5><small>2800 Plays</small></div></div>

<section class="newsletter">
  <h2 class="section-title">Newsletter Subscription</h2>
  <div class="title-rule" style="top:160px"></div>
  <p class="news-text">We are launching a Weekly Lantern Lane from a different place in the world</p>
  <p class="news-small">libero, faucibus adipiscing, commodo quis, gravida lorem ipsum.</p>
</section>
<div class="email-box">Enter the Email</div>
<a class="btn-red subscribe">Subscribe</a>

<footer class="footer">
  <div class="foot-col" style="left:99px"><h6>About</h6><ul><li>The Company</li><li>Our Values</li><li>Responsibility</li><li>Our Mission</li><li>Opportunity</li></ul></div>
  <div class="foot-col" style="left:323px"><h6>Top Destinations</h6><ul><li>Netherlands</li><li>Nepal</li><li>Canada</li><li>France</li><li>Germany</li><li>United Kingdom</li></ul></div>
  <div class="foot-col" style="left:650px"><h6>Booking Terms</h6><ul><li>Booking Conditions</li><li>My Bookings</li><li>Refund Policy</li><li>Includes &amp; Excludes</li><li>Your Responsibilities</li><li>Order a Brochure</li></ul></div>
  <div class="foot-col contact" style="left:931px"><h6>Contact</h6><ul>
    <li><svg width="10" height="10" viewBox="0 0 10 10"><path d="M2 0l2 2-1 2 3 3 2-1 2 2-2 2C4 10 0 6 0 2z" fill="#fff"/></svg>(0100) 555 0142</li>
    <li style="padding-left:18px">(0100) 555 0178</li>
    <li><svg width="10" height="8" viewBox="0 0 10 8"><rect width="10" height="8" fill="#fff"/><path d="M0 0l5 4 5-4" fill="none" stroke="#000"/></svg>support@lanternlane.example</li>
    <li><svg width="10" height="10" viewBox="0 0 10 10"><path d="M5 0a3.5 3.5 0 0 1 3.5 3.5C8.5 6 5 10 5 10S1.5 6 1.5 3.5A3.5 3.5 0 0 1 5 0z" fill="#fff"/></svg>Lantern Lane</li>
    <li style="padding-left:18px">Lorem Ipsum</li>
  </ul>
  <div class="social"><span>Chatterbook</span><span>Chirplet</span><span>Snapfolio</span></div></div>
  <div class="foot-bar"></div>
  <p class="copyright">Copyright © 2017 Lantern Lane. All Rights Reserved.</p>
  <div class="pay"><span>Cardvale</span><span>Duocard</span><span>Purselink</span><span>Ambercharge</span></div>
</footer>

</body>
</html>
```